We need your help in designing the graphical look of the home page of our web site: Quellnest.com.

Quellnest is an FREE online service that brings consumers and service providers together through online reservations.

Our service is in fact a web application (similar to brindlo calendar), so we will be using forms, widgets, menus and standard web controls (buttons, fields, links, etc). We need a design that will be easy to integrate with our programming.

This design project is for the HOME page, but we will choose the designer that will design the web page in photoshop in layers, so we can easily derive our other secondary pages ourselves.

If you have any questions please send us a message and we will gladly update the brief with a response.

Happy Designing!
Updates

Hi all, the menu on the home page should be something standard, like: Pricing, features, how it works.

once a user is logged in, they will see their toolbox at all times:
- My Nest (links to their main page of bookings)
- My Faborites (view favorite businesses and book quickly with them)
- Settings (set parameters of their account)

There should be a My Profile page as well. 

Thanks!

Reason: I have extended the deadline to receive more designs.

Hi All,

UPDATE: we changed our vision of the home page to have a much simpler design.  something along the lines of tumbrella vexnor and mor tan.

HOME PAGE:
light colors with white background.  simple, simple, simple!

header should not be big, logo, change language link. try with search bar (what and where).

body should be simple, with an image + register form only.

footer with links to pages for more info:
- Privacy,
- Getting started
- How it works
- Contact us
- FAQ
- Pricing

LOGGED IN PAGE:
when logged in, the header can be the same or reduced to maximize the "working area" (body).
body can be a 2 or 3 column design, as we have a main working area.  in your design, show a calendar.  we need a toolbar (side or top) that will have these buttons, links: MyNest, My Favorites, Settings, My Profile.
We need a section that will display latest messages or notifications.
keep the footer with the links.

Thank you all.

Reason: Holidays

Reason: holidays... lets spend time with our families!

Target Market(s)

Young and mobile consumers + professionals, businesses, restaurants and commerces wishing to offer online reservations (appointments and reservations)

Industry/Entity Type

Brindlo

Requirements
Must have
• - Easy to integrate with web programming
- light weight visual design. We want something with light tone colors as background
- home page will have a content slider that will show some catch phrases.
- Overall design should be more on the "cartoony" side. Should give a casual, humour and friendly ambiance.

The home page should have these sections:
- a search section for consumers to find local businesses. They will search by specifying "What?" & "Where?"
- a content slider that will cycle through catch phrases and features. Each pane should have an image representative of the text.
- have 4 highlighted sections
- QuellNest is great for (list of different businesses types that use quelnest)
- QuellNest is available for FREE to everyone
- Main features list (accept 24/7 reservations, never reveal your schedule, automatic reminders, marketing campaigns)
- The more you quell, the more you save! (info on our loyalty program that entitles consumers to greater savings and benefits).

One a user logs in, all the certer page info will be replaced by a content div that will allow content to display based on selected menu item
- My Nest (opens the main section where all happens. This section should have a design that gives the impression that we're looking in a box)
- My Profile
- My Favorites
Should not have
• - Don't use actual photos of real people, rather opt for sketches and cartoony characters.

```html
<!DOCTYPE html>
<html lang="en">
<head>
<meta charset="utf-8">
<title>QuellNest – Schedule can be easy</title>
<link href="https://fonts.googleapis.com/css2?family=Arimo:wght@400&family=Cabin+Sketch:wght@700&family=PT+Sans:wght@400;700&display=swap" rel="stylesheet">
<style>
  :root{
    --header-top:#ffffff;
    --header-bottom:#d9d9d9;
    --body-top:#1ba5c6;
    --body-bottom:#38e6f5;
    --brand:#1e9cbf;
    --ink:#111111;
    --field:#d3f3f8;
    --field-edge:#9fdbe6;
    --footer:#000000;
    --footer-text:#f2f2f2;
  }
  *{box-sizing:border-box;margin:0;padding:0}
  html,body{width:1200px;height:888px;overflow:hidden}
  body{position:relative;font-family:"PT Sans",sans-serif;color:var(--ink);
    background:linear-gradient(180deg,var(--body-top) 122px,var(--body-bottom) 772px)}

  .site-header{position:absolute;left:0;top:0;width:1200px;height:122px;
    background:linear-gradient(180deg,var(--header-top),var(--header-bottom));
    box-shadow:0 2px 4px rgba(0,0,0,.25)}
  .brand{position:absolute;left:120px;top:40px;display:flex;align-items:center;gap:10px;
    font-weight:700;font-size:30px;color:var(--brand);text-decoration:none}
  .brand-mark{width:34px;height:34px;background:var(--brand)}
  .account-links{position:absolute;left:893px;top:12px;font-family:"Arimo",sans-serif;font-size:15px}
  .account-links .login{color:var(--brand);text-decoration:none}
  .account-links .or{margin-left:6px}
  .register{position:absolute;left:977px;top:0;width:94px;height:43px;background:var(--brand);
    color:#fff;font-family:"Arimo",sans-serif;font-size:15px;display:flex;align-items:center;justify-content:center;
    border-radius:0 0 4px 4px;box-shadow:2px 2px 3px rgba(0,0,0,.3);text-decoration:none}
  .main-nav a{position:absolute;top:74px;font-family:"Arimo",sans-serif;font-size:15px;color:var(--ink);text-decoration:none}

  .headline{position:absolute;left:0;top:158px;width:1162px;text-align:center;
    font-family:"Cabin Sketch",sans-serif;font-weight:700;font-size:64px;color:#000;line-height:1}

  .hero-visual{position:absolute;left:131px;top:248px;width:366px;height:511px;border-radius:40px;
    background:linear-gradient(180deg,#1f2226 0%,#3a3f45 60%,rgba(60,70,80,.2) 100%)}

  .signup{position:absolute;left:614px;top:266px;width:440px;height:460px}
  .signup h1{font-size:24px;font-weight:400;letter-spacing:.5px;line-height:1.1}
  .signup p{font-size:20px;line-height:1.1}
  .form-row{position:absolute;left:0;width:440px;height:35px}
  .form-row label{position:absolute;left:-30px;top:0;width:121px;height:35px;line-height:35px;
    text-align:right;font-size:15px;white-space:nowrap}
  .field{position:absolute;left:109px;top:0;height:35px;background:var(--field);border:1px solid var(--field-edge);border-radius:2px}
  .text-field{width:319px}
  .select{display:flex;align-items:center;padding-left:10px;font-size:15px}
  .select::after{content:"";position:absolute;right:0;top:0;width:24px;height:33px;border-left:1px solid var(--field-edge)}
  .select svg{position:absolute;right:8px;top:12px}
  .submit{position:absolute;left:110px;top:407px;width:117px;height:38px;border-radius:19px;background:#b5eef5;
    display:flex;align-items:center;justify-content:center}
  .submit span{display:block;width:107px;height:28px;border-radius:14px;background:linear-gradient(#eefcfe,#bdebf3);
    font-size:18px;text-align:center;line-height:28px}

  .site-footer{position:absolute;left:0;top:772px;width:1200px;height:116px;background:var(--footer);color:var(--footer-text);font-size:12px}
  .footer-col{position:absolute;top:13px;list-style:none;line-height:17px}
  .footer-col a{color:var(--footer-text);text-decoration:none}
  .social{position:absolute;left:422px;top:13px}
  .social ul{list-style:none;display:flex;gap:16px;margin-top:12px;font-size:13px;font-weight:700;color:#bfeef6}
  .copyright{position:absolute;left:834px;top:13px}
  .copyright span{color:var(--brand)}
</style>
</head>
<body>
<header class="site-header">
  <a class="brand" href="#"><span class="brand-mark"></span>QuellNest</a>
  <div class="account-links"><a class="login" href="#">LOGIN</a><span class="or">OR</span></div>
  <a class="register" href="#">REGISTER</a>
  <nav class="main-nav">
    <a href="#" style="left:531px">HOME</a>
    <a href="#" style="left:620px">FEATURES</a>
    <a href="#" style="left:741px">PRICING</a>
    <a href="#" style="left:846px">PURCHASE</a>
    <a href="#" style="left:966px">SUPPORT</a>
  </nav>
</header>

<h2 class="headline">SCHEDULE can be easy</h2>

<div class="hero-visual" role="img" aria-label="Smartphone showing a December calendar with a magnifying glass over it"></div>

<section class="signup">
  <h1>SIGN UP</h1>
  <p>register to manage your schedule easily</p>
  <form>
    <div class="form-row" style="top:72px"><label>First Name</label><div class="field text-field"></div></div>
    <div class="form-row" style="top:119px"><label>Last Name</label><div class="field text-field"></div></div>
    <div class="form-row" style="top:166px"><label>Your Email</label><div class="field text-field"></div></div>
    <div class="form-row" style="top:213px"><label>Re-enter Email</label><div class="field text-field"></div></div>
    <div class="form-row" style="top:260px"><label>Password</label><div class="field text-field"></div></div>
    <div class="form-row" style="top:307px"><label>I am</label>
      <div class="field select" style="width:122px">Select Sex<svg width="7" height="10"><path d="M0 4 3.5 0 7 4ZM0 6 3.5 10 7 6Z" fill="#6a8a90"/></svg></div></div>
    <div class="form-row" style="top:354px"><label>Birthday</label>
      <div class="field select" style="width:94px">Month<svg width="7" height="10"><path d="M0 4 3.5 0 7 4ZM0 6 3.5 10 7 6Z" fill="#6a8a90"/></svg></div>
      <div class="field select" style="left:212px;width:75px">Day<svg width="7" height="10"><path d="M0 4 3.5 0 7 4ZM0 6 3.5 10 7 6Z" fill="#6a8a90"/></svg></div>
      <div class="field select" style="left:296px;width:84px">Year<svg width="7" height="10"><path d="M0 4 3.5 0 7 4ZM0 6 3.5 10 7 6Z" fill="#6a8a90"/></svg></div>
    </div>
    <div class="submit"><span>Sign Up</span></div>
  </form>
</section>

<footer class="site-footer">
  <ul class="footer-col" style="left:131px">
    <li><a href="#">Pricing</a></li><li><a href="#">How it works</a></li><li><a href="#">Priivacy</a></li>
    <li><a href="#">Contact us</a></li><li><a href="#">Terms of service</a></li>
  </ul>
  <ul class="footer-col" style="left:272px">
    <li><a href="#">Getting started</a></li><li><a href="#">FAQ</a></li><li><a href="#">Loyalty program</a></li><li><a href="#">Features</a></li>
  </ul>
  <div class="social">JOIN US ON
    <ul><li>vexnor</li><li>tumbrella</li><li>mor tan</li></ul>
  </div>
  <p class="copyright">Copyright (c) 2011 <span>QuellNest</span>. All rights reserved.</p>
</footer>
</body>
</html>
```